KPT Building And Maintenance

Need a very professional looking double sided Buisiness card with all my details phone number, name, email, license number.

Target Market(s)

construction industry

Industry/Entity Type

building

Contact Information for Business Card

Name Dale Whitcombe. Email Address Info@KPTBuilding.example.au mobile number 0452918730 licence number 871406D. web site

```html
<!DOCTYPE html>
<html lang="en">
<head>
<meta charset="utf-8">
<title>KPT Building And Maintenance – Business Card</title>
<link rel="stylesheet" href="https://fonts.googleapis.com/css2?family=Arimo:wght@400;700&display=swap">
<style>
  :root {
    --backdrop: #d9d9db;
    --card-white: #ffffff;
    --card-charcoal: #3b3c3e;
    --accent-blue: #1b95e0;
    --text-light: #f2f2f2;
    --logo-grey: #3b3c3e;
  }
  * { margin: 0; padding: 0; box-sizing: border-box; }
  html, body {
    width: 1200px; height: 800px; overflow: hidden;
    background: var(--backdrop);
    font-family: "Arimo", Arial, sans-serif;
  }
  .canvas {
    position: relative; width: 1200px; height: 800px;
    display: flex; align-items: center; justify-content: center; gap: 40px;
  }
  .card {
    position: relative; width: 540px; height: 330px;
    border-radius: 22px; overflow: hidden;
    box-shadow: 0 10px 24px rgba(0,0,0,0.18);
  }
  /* Front */
  .card-front { background: var(--card-white); }
  .front-panels { position: absolute; inset: 0; }
  .front-logo {
    position: absolute; left: 34px; top: 118px;
    display: flex; align-items: center; gap: 10px;
  }
  .logo-square { width: 16px; height: 16px; background: var(--accent-blue); flex: none; }
  .logo-name {
    font-weight: 700; font-size: 26px; line-height: 30px;
    color: var(--logo-grey); letter-spacing: 0.5px;
  }
  .logo-name-line { display: block; }
  .contact-block {
    position: absolute; right: 30px; top: 100px;
    text-align: right; color: var(--text-light);
  }
  .contact-name {
    font-weight: 700; font-size: 20px; color: var(--accent-blue);
    text-transform: uppercase; letter-spacing: 0.5px; margin-bottom: 8px;
  }
  .contact-line {
    display: flex; justify-content: flex-end; align-items: center; gap: 8px;
    font-size: 13px; line-height: 20px;
  }
  .contact-icon { width: 11px; height: 11px; flex: none; }
  .icon-spacer { width: 11px; flex: none; }
  /* Back */
  .card-back {
    background: var(--card-charcoal);
    display: flex; flex-direction: column; align-items: center; justify-content: center;
  }
  .back-logo {
    display: flex; align-items: center; gap: 14px; margin-bottom: 44px;
  }
  .back-logo .logo-square { width: 26px; height: 26px; }
  .back-logo .logo-name { font-size: 46px; line-height: 52px; color: var(--accent-blue); }
  .back-website {
    font-size: 14px; color: var(--text-light);
    letter-spacing: 5px; text-transform: uppercase;
  }
</style>
</head>
<body>
<main class="canvas">
  <section class="card card-front" aria-label="Business card front">
    <svg class="front-panels" width="540" height="330" viewBox="0 0 540 330" aria-hidden="true">
      <polygon points="540,38 262,72 150,330 540,330" fill="var(--accent-blue)"/>
      <polygon points="540,46 270,80 160,330 540,330" fill="var(--card-white)"/>
      <polygon points="540,54 280,86 172,330 540,330" fill="var(--card-charcoal)"/>
    </svg>
    <div class="front-logo">
      <span class="logo-square"></span>
      <span class="logo-name"><span class="logo-name-line">KPT</span><span class="logo-name-line">Building</span></span>
    </div>
    <div class="contact-block">
      <p class="contact-name">Dale Whitcombe</p>
      <p class="contact-line">0452918730
        <svg class="contact-icon" viewBox="0 0 12 12"><path d="M2.4 0.8 L4.4 0.5 L5.3 3.3 L4 4.3 C4.6 5.7 6.3 7.4 7.7 8 L8.7 6.7 L11.5 7.6 L11.2 9.6 C11 10.8 10 11.4 8.8 11.2 C4.8 10.4 1.6 7.2 0.8 3.2 C0.6 2 1.2 1 2.4 0.8 Z" fill="var(--accent-blue)"/></svg>
      </p>
      <p class="contact-line">Info@KPTBuilding.example.au
        <svg class="contact-icon" viewBox="0 0 12 12"><rect x="0.5" y="2" width="11" height="8" fill="var(--accent-blue)"/><polyline points="0.5,2 6,7 11.5,2" fill="none" stroke="var(--card-charcoal)" stroke-width="1"/></svg>
      </p>
      <p class="contact-line">KPTBuilding.example.au
        <svg class="contact-icon" viewBox="0 0 12 12"><circle cx="6" cy="6" r="5.5" fill="var(--accent-blue)"/></svg>
      </p>
      <p class="contact-line">Lic No: 871406D<span class="icon-spacer"></span></p>
    </div>
  </section>

  <section class="card card-back" aria-label="Business card back">
    <div class="back-logo">
      <span class="logo-square"></span>
      <span class="logo-name">KPT Building</span>
    </div>
    <p class="back-website">www.kptbuilding.example.au</p>
  </section>
</main>
</body>
</html>
```